ONE Unique Graphic of (A real estate sales funnel)

I’m looking for someone to create a very simple but effective graphic representation of this drawing to represent my real estate sales funnel I am using this graphic to explain to real estate agents what a sales funnel is and does.

For more information check out my webpage

http://www.brightquillinstitute.com/welcome

I am still working on but most of the information you need is there this is not a live page but I am currently working on finishing it this weekend. The website should give you an idea of my colors and I like things clean and simple less is more

Deliverabel: ONE GRAPHIC, simple transparent background and with top label "Real Estate Sales Funnel"

```html
<!DOCTYPE html>
<html lang="en">
<head>
<meta charset="utf-8">
<title>Real Estate Sales Funnel</title>
<link href="https://fonts.googleapis.com/css2?family=Montserrat:wght@800&family=Oswald:wght@700&family=Roboto:wght@700&display=swap" rel="stylesheet">
<style>
  :root {
    --bg: #ffffff;
    --title: #4d4d4d;
    --band: #5fbf7a;
    --throat: #2b3b47;
    --tag: #3fb25c;
    --white: #ffffff;
    --channel: #3a4a56;
    --channel-alt: #7a8791;
    --screen: #f2c13b;
    --coin: #f3b73b;
    --coin-dark: #d9952a;
  }
  html, body { margin: 0; padding: 0; overflow: hidden; background: var(--bg); }
  .canvas { width: 1200px; height: 1199px; display: block; }
  .title { font-family: "Montserrat", sans-serif; font-weight: 800; fill: var(--title); }
  .stage-name { font-family: "Oswald", sans-serif; font-weight: 700; fill: var(--white); }
  .tag-text { font-family: "Roboto", sans-serif; font-weight: 700; fill: var(--white); }
  .channel-name { font-family: "Roboto", sans-serif; font-weight: 700; fill: var(--white); font-size: 7px; }
  .channel-dot { fill: var(--channel); }
  .channel-dot.alt { fill: var(--channel-alt); }
  .band { fill: var(--band); }
  .throat { fill: var(--throat); }
  .tag { fill: var(--tag); }
</style>
</head>
<body>
<svg class="canvas" viewBox="0 0 900 899.25" xmlns="http://www.w3.org/2000/svg">
  <text class="title" x="452" y="268" font-size="36" text-anchor="middle">REAL ESTATE SALES FUNNEL</text>

  <g class="channels">
    <g class="desktop">
      <rect x="455" y="315" width="70" height="46" rx="3" fill="#4a5560"/>
      <rect x="461" y="321" width="58" height="34" fill="var(--screen)"/>
      <rect x="482" y="361" width="16" height="8" fill="#8a9299"/>
    </g>
    <circle class="channel-dot" cx="362" cy="345" r="17"/><text class="channel-name" x="362" y="347.5" text-anchor="middle">Orla</text>
    <circle class="channel-dot alt" cx="407" cy="340" r="15"/><text class="channel-name" x="407" y="342.5" text-anchor="middle">Kesto</text>
    <circle class="channel-dot" cx="435" cy="377" r="17"/><text class="channel-name" x="435" y="379.5" text-anchor="middle">Mirvo</text>
    <circle class="channel-dot" cx="552" cy="316" r="19"/><text class="channel-name" x="552" y="318.5" text-anchor="middle">Talen</text>
    <circle class="channel-dot alt" cx="545" cy="361" r="15"/><text class="channel-name" x="545" y="363.5" text-anchor="middle">Brevi</text>
    <rect class="channel-dot alt" x="565" y="359" width="30" height="26" rx="4"/>
    <rect class="channel-dot alt" x="372" y="376" width="28" height="24" rx="4"/>
    <circle class="channel-dot alt" cx="525" cy="404" r="15"/>
  </g>

  <g class="funnel">
    <ellipse class="throat" cx="475" cy="397" rx="140" ry="14"/>
    <path class="band" d="M335 397 Q475 425 615 397 L590 462 Q475 490 355 462 Z"/>
    <text class="stage-name" x="472" y="456" font-size="31" text-anchor="middle">LEAD CAPTURE</text>

    <ellipse class="throat" cx="474" cy="485" rx="112" ry="11"/>
    <path class="band" d="M362 485 Q474 507 586 485 L570 535 Q474 555 378 535 Z"/>
    <text class="stage-name" x="474" y="527" font-size="21" text-anchor="middle">CUSTOMER JOURNEY</text>

    <ellipse class="throat" cx="474" cy="557" rx="92" ry="10"/>
    <path class="band" d="M382 557 Q474 577 566 557 L552 600 Q474 616 396 600 Z"/>
    <text class="stage-name" x="475" y="594" font-size="24" text-anchor="middle">CONVERSATION</text>

    <ellipse class="throat" cx="472" cy="619" rx="74" ry="9"/>
    <path class="band" d="M398 619 Q472 637 546 619 L535 658 Q472 672 410 658 Z"/>
    <text class="stage-name" x="473" y="655" font-size="19" text-anchor="middle">BUY/SELL</text>
  </g>

  <g class="tags">
    <path class="tag" d="M175 343 H316 L328 360 L316 377 H175 Z"/>
    <text class="tag-text" x="249" y="366" font-size="15" text-anchor="middle">TRAFFIC/PEOPLE</text>
    <path class="tag" d="M257 415 H343 L355 433 L343 452 H257 Z"/>
    <text class="tag-text" x="302" y="441" font-size="19" text-anchor="middle">LEADS</text>
    <path class="tag" d="M275 497 H370 L380 513 L370 530 H275 Z"/>
    <text class="tag-text" x="326" y="519" font-size="14" text-anchor="middle">PROSPECTS</text>
    <path class="tag" d="M293 565 H383 L393 580 L383 596 H293 Z"/>
    <text class="tag-text" x="341" y="586" font-size="13" text-anchor="middle">CUSTOMERS</text>
    <path class="tag" d="M333 625 H405 L415 640 L405 656 H333 Z"/>
    <text class="tag-text" x="370" y="646" font-size="14" text-anchor="middle">CLIENTS</text>
  </g>

  <defs>
    <linearGradient id="coinFill" x1="0" y1="0" x2="0" y2="1">
      <stop offset="0" stop-color="var(--coin)"/>
      <stop offset="1" stop-color="var(--coin-dark)"/>
    </linearGradient>
  </defs>
  <g role="img" aria-label="Stacks of gold coins topped with small houses">
    <rect x="432" y="690" width="26" height="52" rx="6" fill="url(#coinFill)"/>
    <rect x="452" y="702" width="30" height="54" rx="6" fill="url(#coinFill)"/>
    <rect x="478" y="686" width="27" height="58" rx="6" fill="url(#coinFill)"/>
  </g>
</svg>
</body>
</html>
```